Business Card Design for a technology company

Our current business card is outdated and stale.

We need a new look and one soon.

We're a telematics (GPS tracking) company based in Australia. Our audiences are transport and logistics company.

Target Market(s)

1. Transport and Logistics Companies
2. Food and Beverage Manufacturers
3. Concrete Businesses

Industry/Entity Type

Logistics

Contact Information for Business Card

Halvor Pinet

Font styles to use
Sans Serif

Colors
3276b5
0255a3
85acd3
cfdeed
ffffff

Requirements
Must have
• Logo
• "Premium Suppliers of Real Time Temperature Tracking"
• Contact Name
• Business Title
• Address
• Telephone
• Mobile
• Email
• Website URL
Nice to have
• Visual representation of tracking or maps.
Should not have
• Image of a satellite as currently shown

```html
<!DOCTYPE html>
<html lang="en">
<head>
<meta charset="utf-8">
<title>Halvor Pinet – Business Card</title>
<link rel="stylesheet" href="https://fonts.googleapis.com/css2?family=Jost:wght@400;500&family=Roboto+Condensed:ital,wght@0,400;0,500;1,500&display=swap">
<style>
  :root {
    --page-bg: #e6e6e6;
    --blue-deep: #0255a3;
    --blue-dark: #033c86;
    --blue-mid: #3276b5;
    --blue-soft: #85acd3;
    --blue-pale: #cfdeed;
    --white: #ffffff;
    --card-back: #f4f4f4;
    --ink: #1c1c1c;
    --shadow: rgba(0, 0, 0, 0.28);
  }
  * { margin: 0; padding: 0; box-sizing: border-box; }
  html, body { width: 1200px; height: 960px; overflow: hidden; }
  body {
    background: var(--page-bg);
    position: relative;
    font-family: "Jost", sans-serif;
  }
  .card {
    position: absolute;
    width: 600px;
    height: 343px;
    box-shadow: 1px 2px 4px var(--shadow);
    overflow: hidden;
  }
  .card-front {
    left: 314px; top: 113px;
    background: linear-gradient(180deg, var(--blue-soft) 0%, var(--blue-mid) 35%, var(--blue-deep) 78%, var(--blue-dark) 100%);
    color: var(--white);
  }
  .card-back {
    left: 311px; top: 472px;
    background: var(--card-back);
  }
  .map-area {
    position: absolute;
    border-radius: 40%;
  }
  .card-front .map-area {
    left: 20px; top: 10px; width: 560px; height: 320px;
    background: radial-gradient(ellipse at center, rgba(255,255,255,0.12) 0%, rgba(255,255,255,0.04) 60%, rgba(255,255,255,0) 75%);
  }
  .card-back .map-area {
    left: 20px; top: 10px; width: 570px; height: 320px;
    background: radial-gradient(ellipse at center, rgba(0,0,0,0.05) 0%, rgba(0,0,0,0.02) 60%, rgba(0,0,0,0) 75%);
  }
  .contact-name {
    position: absolute;
    left: 44px; top: 50px;
    font-size: 20px;
    font-weight: 400;
    letter-spacing: 0.3px;
  }
  .contact-block {
    position: absolute;
    left: 44px;
    font-size: 14.5px;
    line-height: 18px;
    font-weight: 400;
  }
  .company-line { top: 112px; }
  .address-line { top: 158px; }
  .contact-list {
    top: 206px;
    list-style: none;
    line-height: 19.3px;
  }
  .contact-list li { display: flex; align-items: center; }
  .contact-list svg { width: 12px; height: 12px; margin-right: 9px; fill: var(--white); flex: none; }
  .brand {
    position: absolute;
    left: 0; right: 0; top: 120px;
    text-align: center;
  }
  .brand-name {
    display: inline-flex;
    align-items: center;
    gap: 12px;
    font-size: 50px;
    font-weight: 500;
    color: var(--blue-deep);
    line-height: 1;
  }
  .brand-dot {
    width: 22px; height: 22px;
    border-radius: 50%;
    background: var(--blue-deep);
  }
  .tagline {
    margin-top: 8px;
    font-family: "Roboto Condensed", sans-serif;
    font-size: 13.5px;
    color: var(--ink);
    font-weight: 500;
  }
  .tagline em { color: var(--blue-deep); }
  .service-band {
    position: absolute;
    left: 0; right: 0; top: 281px; height: 32px;
    background: linear-gradient(90deg, var(--blue-dark) 0%, var(--blue-mid) 50%, var(--blue-dark) 100%);
    color: var(--white);
    font-family: "Roboto Condensed", sans-serif;
    font-size: 15px;
    letter-spacing: 0.3px;
    display: flex; align-items: center; justify-content: center;
  }
</style>
</head>
<body>
  <section class="card card-front">
    <div class="map-area" role="img" aria-label="Faint world map in the background"></div>
    <h1 class="contact-name">DORIAN KESSEL</h1>
    <p class="contact-block company-line">Halvor Pinet Rentals Pty Ltd<br>ABN: 48 602 317 594</p>
    <p class="contact-block address-line">4,18 Larkin Street<br>Ringwood VIC 3134</p>
    <ul class="contact-block contact-list">
      <li><svg viewBox="0 0 12 12"><path d="M2.5 0.5l2 2.5-1 1.2c.7 1.5 1.8 2.6 3.3 3.3l1.2-1 2.5 2-1 2C5.5 10.3 1.7 6.5 0.5 2.5z"/></svg>+61 3 9514 2280</li>
      <li><svg viewBox="0 0 12 12"><path d="M3 0h6v12H3zM4 1.5v8h4v-8z"/></svg>0412 607 335</li>
      <li><svg viewBox="0 0 12 12"><path d="M3 0h6v3H3zM0 4h12v5h-2v3H2V9H0zM3 8v3h6V8z"/></svg>+61 3 9514 2281</li>
      <li><svg viewBox="0 0 12 12"><path d="M0 2h12v8H0zM1 3l5 3.5L11 3v-.2H1z"/></svg>dkessel@halvorpinet.com.au</li>
      <li><svg viewBox="0 0 12 12"><circle cx="6" cy="6" r="6"/></svg>www.halvorpinet.com.au</li>
    </ul>
  </section>

  <section class="card card-back">
    <div class="map-area" role="img" aria-label="Faint world map in the background"></div>
    <div class="brand">
      <div class="brand-name"><span class="brand-dot"></span>Halvor Pinet</div>
      <p class="tagline">Your eye in the sky <em>Watch and Monitor on the Web 24/7</em></p>
    </div>
    <div class="service-band">PREMIUM SUPPLIERS OF REAL TIME TEMPERATURE TRACKING</div>
  </section>
</body>
</html>
```